Premium Personal Brand — Facebook Banner (Used Across All Platforms)

Update — Additional Color Direction
In addition to the dark charcoal/slate direction already described, I'm also interested in seeing variants with:
Dark navy blue — Deep, authoritative, intelligence-community feel. Same textured/matte treatment, not flat or bright.
Warm charcoal with steel blue accent — Keep the dark base but introduce a subtle steel blue gradient, accent line, or tonal shift. Sophisticated, modern, adds dimension without adding color noise.
Both should maintain the same premium, restrained, architectural feel described in the original brief. No bright blues, no corporate PowerPoint energy — think midnight, think depth, think weight.
Everything else in the brief remains the same.
I am building a premium personal brand as an executive advisor to founders ($5M+ revenue).
This contest is Facebook-banner–focused, but the design must represent a visual system that will be reused across:
- LinkedIn
- YouTube
I- nstagram
- X (Twitter)
- Website hero sections and other brand touchpoints
Think of the Facebook banner as the primary expression of the brand — not a one-off graphic.
This project is about discovering a high-end visual style and brand feel, not decoration.
What to design
Please submit one cohesive visual system, shown primarily as:
- Facebook banner (primary focus)
The same design language should clearly translate to all platforms listed above.
Designers are responsible for using the current recommended dimensions for each platform.
Quick clarification on background direction:
Backgrounds should have depth and texture, not flat color fields. Avoid pure white, light grey, or solid black backgrounds. Think matte, architectural materials — stone, graphite, concrete, steel — not blank canvases. Subtle tonal variation is encouraged. Obvious gradients or decorative patterns are not.
Text to use
Primary Headline:
- Your Business Is Too Valuable To Be Run On Hope.
Subheadline:
- You didn’t build a business to become its prisoner.
Name:
Paul Whitaker
The headline should be the dominant visual element.
Logo note (important)
My personal logo is currently being finalized.
For this contest:
- Use a simple “PW” monogram placeholder
- Clean, bold, geometric sans-serif
- Do not design a logo
- The winning design must allow an easy logo swap later.
Headshot note (important)
- Please do not include a headshot in the banner design.
- Most platforms display a circular profile image separately.
- The banner should stand on its own using typography, layout, and tone only.
- Design the banner assuming the profile photo will sit nearby, not inside the banner.
Style direction
The design should feel:
- Premium
- Calm
- Confident
- Restrained
- High-trust
- Dark, neutral backgrounds are preferred.
- Fewer elements are better than more.
Think:
- Owner-level advisor
- Private equity / boardroom tone
- Industrial, Modern, Minimalist, Elite, Architectural, not decorative
What to avoid
Please do not submit designs that feel:
- Promotional, hype-driven, or salesy
- Like a coach, guru, or agency
- Bright, colorful, or gradient-heavy
- Busy or over-designed
- Based on stock photos
- No motivational speaker energy.
Reaction test
- If someone sees this banner on Facebook (or later on LinkedIn, YouTube, etc.), the reaction should be:
“That person is serious. I’d trust them with important decisions.”
Final note
- I am not looking for many variations.
- I am looking for one strong visual direction you believe in.
Simple beats clever.
- Restraint beats decoration.

```html
<!DOCTYPE html>
<html lang="en">
<head>
<meta charset="utf-8">
<title>Paul Whitaker — Banner</title>
<link rel="stylesheet" href="https://fonts.googleapis.com/css2?family=Montserrat:wght@300;500;800&display=swap">
<style>
  :root {
    --bg-deep: #17191c;
    --bg-base: #24272b;
    --bg-lift: #34383d;
    --headline: #e4e4e2;
    --subline: #9ba4ad;
    --monogram: #56616c;
    --name: #b9c2cb;
    --rule: #7f93a6;
  }
  html, body {
    margin: 0;
    padding: 0;
    overflow: hidden;
    background: var(--bg-deep);
  }
  .banner {
    position: relative;
    width: 1200px;
    height: 444px;
    overflow: hidden;
    font-family: "Montserrat", sans-serif;
    background:
      radial-gradient(ellipse 60% 80% at 78% 30%, rgba(120,135,150,0.10) 0%, rgba(120,135,150,0) 70%),
      radial-gradient(ellipse 50% 70% at 15% 85%, rgba(0,0,0,0.35) 0%, rgba(0,0,0,0) 70%),
      repeating-linear-gradient(90deg, rgba(255,255,255,0.012) 0px, rgba(255,255,255,0.012) 1px, rgba(0,0,0,0) 1px, rgba(0,0,0,0) 3px),
      repeating-linear-gradient(0deg, rgba(0,0,0,0.03) 0px, rgba(0,0,0,0.03) 1px, rgba(0,0,0,0) 1px, rgba(0,0,0,0) 4px),
      linear-gradient(100deg, var(--bg-deep) 0%, var(--bg-base) 45%, var(--bg-lift) 100%);
  }
  .monogram {
    position: absolute;
    left: 62px;
    top: 134px;
    margin: 0;
    font-size: 150px;
    line-height: 1;
    font-weight: 800;
    letter-spacing: -0.04em;
    color: var(--monogram);
  }
  .headline {
    position: absolute;
    right: 229px;
    top: 116px;
    margin: 0;
    font-size: 66px;
    line-height: 62px;
    font-weight: 800;
    letter-spacing: -0.025em;
    color: var(--headline);
    text-align: right;
  }
  .headline span { display: block; white-space: nowrap; }
  .subline {
    position: absolute;
    right: 229px;
    top: 306px;
    margin: 0;
    font-size: 21px;
    line-height: 24px;
    font-weight: 300;
    letter-spacing: 0.01em;
    color: var(--subline);
    white-space: nowrap;
  }
  .rule {
    position: absolute;
    left: 356px;
    top: 341px;
    width: 616px;
    height: 3px;
    background: linear-gradient(90deg, rgba(127,147,166,0) 0%, rgba(127,147,166,0.55) 40%, var(--rule) 100%);
  }
  .name {
    position: absolute;
    right: 229px;
    top: 356px;
    margin: 0;
    font-size: 13px;
    line-height: 16px;
    font-weight: 500;
    letter-spacing: 0.32em;
    text-transform: uppercase;
    color: var(--name);
    white-space: nowrap;
    margin-right: -0.32em;
  }
</style>
</head>
<body>
  <div class="banner">
    <p class="monogram" aria-label="Paul Whitaker monogram">PW</p>
    <h1 class="headline">
      <span>Your Business Is</span>
      <span>Too Valuable To Be</span>
      <span>Run On Hope</span>
    </h1>
    <p class="subline">You didn’t build a business to become its prisoner</p>
    <div class="rule"></div>
    <p class="name">Paul Whitaker</p>
  </div>
</body>
</html>
```